Brand Design/Redesign

Design and/or redesign an identity for product and organisation
Create visual identity (colours, fonts), website, mobile app, web application, online campaigns, social media.

I have given a sample wireframe for you to use so that we can really get a sense of the colour palette you are choosing and how it will look in a live context.

Considerations when Choosing:
Brand is for Gen Z -
With a particular focus on 16 - 18 years old.

There will be a commercial portal for Business to use also.

Please outline in a short paragraph why you choose the colours and their relationship to our target audience.

Selected winner to produce Brand Identity Document

Please see document attached.

Target Market(s)

Gen Z 16 - 18 yearolds

Industry/Entity Type

Social Media

Requirements
Must have
• Colour Palette & Font Selections, Visual of Colour Palette & Winner to produce Brand Identity Doc
Nice to have
• Really Cool, Edgy and Appeal to aYoung Audience
Should not have
• A corporate feel to it

```html
<!DOCTYPE html>
<html lang="en">
<head>
<meta charset="utf-8">
<title>Zubvi — App Identity Screens</title>
<link href="https://fonts.googleapis.com/css2?family=Rubik:wght@400;500;700&display=swap" rel="stylesheet">
<style>
:root{
  --night:#14061a;
  --plum-deep:#250a2e;
  --plum:#3a0f47;
  --plum-card:#3a0d48;
  --pink:#f0449a;
  --hot-pink:#ff3d8a;
  --violet:#b03ce0;
  --violet-soft:#c44ee8;
  --white:#ffffff;
  --ink:#1d1424;
  --grey-bg:#f3f1f4;
  --gold:#ffd23a;
}
*{box-sizing:border-box;margin:0;padding:0}
html,body{width:988px;height:1200px;overflow:hidden;background:var(--night)}
body{font-family:'Rubik',sans-serif}
.stage{position:absolute;left:0;top:0;width:1580px;height:1920px;transform:scale(.625);transform-origin:0 0;background:var(--night);overflow:hidden}
.blob{position:absolute;border-radius:50%}
.blob--pink{left:-420px;top:-560px;width:950px;height:1050px;background:var(--pink)}
.blob--violet{left:1090px;top:1460px;width:1100px;height:900px;background:var(--violet-soft)}

.screen{position:absolute;width:375px;height:800px;overflow:hidden}
.screen--dark{background:var(--plum-deep);color:var(--white)}
.screen--light{background:var(--grey-bg);color:var(--ink)}

.topbar{position:absolute;left:0;top:0;width:100%;height:57px;display:flex;align-items:center;justify-content:space-between;padding:0 22px}
.screen--dark .topbar{background:var(--plum-deep)}
.screen--light .topbar{background:#f0eef1}
.topbar svg{width:20px;height:20px}
.wordmark{font-weight:700;font-size:24px;color:var(--pink);letter-spacing:1px}

.photo{position:absolute;left:25px;top:87px;width:324px;height:287px;border-radius:6px;background:linear-gradient(135deg,#8a7a8f,#3e4c6e 55%,#c9b9d6)}

.about{position:absolute;left:0;top:405px;width:100%;height:330px;border-radius:20px 20px 0 0;padding:26px 31px 0;text-align:center}
.screen--dark .about{background:var(--plum)}
.screen--light .about{background:var(--hot-pink);color:var(--white)}
.about h2{font-size:18px;font-weight:500}
.about .rule{width:34px;height:3px;background:var(--pink);margin:10px auto 24px;border-radius:2px}
.screen--light .about .rule{background:var(--white)}
.about p{font-size:12.6px;line-height:21px;text-align:justify;text-align-last:center}

.tabbar{position:absolute;left:0;bottom:0;width:100%;height:75px;display:flex;justify-content:space-around;align-items:center;padding-top:6px}
.screen--dark .tabbar{background:var(--plum-deep)}
.screen--light .tabbar{background:var(--white)}
.tab{display:flex;flex-direction:column;align-items:center;gap:6px;font-size:12px}
.tab svg{width:26px;height:26px}
.screen--light .tab svg{stroke:var(--pink)}

.login{display:flex;flex-direction:column;align-items:center}
.login--dark{background:linear-gradient(170deg,#ee4fa6 0%,#d84bc0 50%,#b33fdc 100%);color:var(--white)}
.login--light{background:linear-gradient(170deg,#f2f0f2,#e9e7ea 60%,#f4f3f5);color:var(--ink)}
.login .brand{margin-top:92px;font-size:64px;font-weight:700;letter-spacing:3px;line-height:1}
.login--dark .brand{color:var(--white)}
.login--light .brand{color:var(--pink)}
.login h1{margin-top:150px;font-size:24px;font-weight:500}
.field{margin-top:14px;width:277px;height:42px;padding:0 17px;display:flex;align-items:center;font-size:13px}
.field:first-of-type{margin-top:28px}
.login--dark .field{background:rgba(255,255,255,.18);color:var(--white)}
.login--light .field{background:var(--white);color:var(--ink)}
.submit{margin-top:21px;width:277px;height:42px;border-radius:21px;display:flex;align-items:center;justify-content:center;font-size:12px;font-weight:500;letter-spacing:.5px}
.login--dark .submit{background:var(--white);color:var(--pink)}
.login--light .submit{background:linear-gradient(90deg,var(--pink),var(--violet));color:var(--white)}
.create{margin-top:22px;font-size:12px;margin-left:8px}
.login--light .create{color:var(--pink)}
.dots{margin-top:98px;display:flex;gap:3px}
.dots i{width:9px;height:9px;border-radius:50%;background:currentColor}
.dots i:first-child{background:none;border:1px solid currentColor}
.login--light .dots{color:#999}

.tabs{position:absolute;left:108px;top:81px;width:160px;height:34px;border-radius:8px;display:flex;padding:2px;font-size:12px;font-weight:500}
.screen--dark .tabs{border:2px solid var(--white)}
.screen--light .tabs{background:var(--white)}
.tabs span{flex:1;display:flex;align-items:center;justify-content:center;border-radius:6px}
.tabs .on{background:var(--violet-soft);color:var(--white)}
.screen--light .tabs span:not(.on){color:var(--violet-soft)}

.card{position:absolute;border-radius:8px}
.screen--dark .card{background:var(--plum-card);border:1px solid #4b1660}
.screen--light .card{background:var(--white);box-shadow:0 4px 14px rgba(90,40,110,.12)}
.challenge{left:22px;width:332px;height:180px;padding:20px 21px}
.challenge h3{font-size:15px;font-weight:500}
.challenge p{margin-top:12px;width:180px;font-size:11px;line-height:20px}
.btn-pill{display:inline-flex;align-items:center;gap:5px;margin-top:12px;padding:0 12px;height:26px;border-radius:5px;background:var(--violet-soft);color:var(--white);font-size:11px}
.rocket{position:absolute;right:12px;top:20px;width:116px;height:145px;border-radius:58px;background:radial-gradient(circle at 50% 45%,#ff4d6b 0 35%,#c54ad8 36% 60%,rgba(0,0,0,0) 62%)}
.screen--light .rocket{background:radial-gradient(circle at 50% 45%,#ff4d6b 0 35%,#ffb6d0 36% 60%,rgba(0,0,0,0) 62%)}

.avatars{display:flex}
.avatars i{width:22px;height:22px;border-radius:50%;background:linear-gradient(135deg,#c9a58f,#6e4a3c);border:2px solid var(--white);margin-right:-8px}
.bell{width:28px;height:28px;border-radius:50%;display:flex;align-items:center;justify-content:center}
.bell svg{width:14px;height:14px}

.discover{position:absolute;left:22px;font-size:20px;font-weight:500}
.brand-card{position:absolute;text-align:center;border-radius:6px}
.screen--dark .brand-card{width:125px;height:140px;background:#2f0c3b;padding-top:10px}
.brand-card h4{font-size:15px;font-weight:500}
.mark{width:34px;height:34px;border-radius:50%;background:var(--white);border:2px solid var(--violet-soft)}
.screen--dark .brand-card .mark{margin:10px auto 0}
.brand-card small{display:block;font-size:9.5px;line-height:15px;font-weight:500;margin-top:7px}
.follow{display:inline-block;margin-top:6px;padding:0 10px;height:18px;line-height:18px;border-radius:9px;background:var(--violet-soft);color:var(--white);font-size:11px;font-weight:500}
.screen--light .brand-card{width:197px;height:97px;background:var(--white);box-shadow:0 3px 12px rgba(90,40,110,.1);text-align:left;padding:9px 0 0 58px}
.screen--light .brand-card .mark{position:absolute;left:12px;top:12px}
.screen--light .brand-card h4{font-size:16px}
.screen--light .brand-card small{font-size:10px;line-height:14px;font-weight:400;margin-top:2px}
</style>
</head>
<body>
<div class="stage">
  <div class="blob blob--pink"></div>
  <div class="blob blob--violet"></div>

  <!-- About, dark -->
  <section class="screen screen--dark" style="left:105px;top:101px">
    <header class="topbar">
      <svg viewBox="0 0 20 20" fill="none" stroke="#fff" stroke-width="2"><path d="M13 4 7 10l6 6"/></svg>
      <span class="wordmark">ZUBVI</span>
      <svg viewBox="0 0 20 20" fill="none" stroke="#fff" stroke-width="2.4"><circle cx="8.5" cy="8.5" r="5.5"/><path d="m13 13 5 5"/></svg>
    </header>
    <div class="photo" role="img" aria-label="Photo of young friends sitting in a row looking at their phones"></div>
    <article class="about">
      <h2>About Zubvi</h2><div class="rule"></div>
      <p>Lorem ipsum dolor sit amet, consectetur adipiscing elit, sed do eiusmod tempor incididunt ut labore et dolore magna aliqua. Quis ipsum suspendisse ultrices gravida. Risus commodo viverra maecenas accumsan lacus vel facilisis. Lorem ipsum dolor sit amet, consectetur adipiscing elit, sed do eiusmod tempor incididunt ut labore et dolore magna aliqua. Quis ipsum suspendisse ultrices gravida. Risus commodo viverra maecenas accumsan lacus vel facilisis.</p>
    </article>
    <nav class="tabbar">
      <div class="tab"><svg viewBox="0 0 26 26" fill="none" stroke="#fff" stroke-width="1.8"><path d="M4 8h18M4 13h18M4 18h18"/></svg>Home</div>
      <div class="tab"><svg viewBox="0 0 26 26" fill="none" stroke="#fff" stroke-width="1.5"><path d="M3 5h20l-1 5H4zM5 10v12h16V10M10 22v-6h6v6"/></svg>Marketplace</div>
      <div class="tab"><svg viewBox="0 0 26 26" fill="none" stroke="#fff" stroke-width="1.5"><rect x="4" y="8" width="18" height="14" rx="2"/><path d="M7 8l9-4 2 4M16 13h6v5h-6z"/></svg>Vault</div>
      <div class="tab"><svg viewBox="0 0 26 26" fill="none" stroke="#fff" stroke-width="1.5"><circle cx="13" cy="13" r="11"/><circle cx="13" cy="10" r="4"/><path d="M6 20c2-4 12-4 14 0"/></svg>Profile</div>
    </nav>
  </section>

  <!-- Login, dark -->
  <section class="screen login login--dark" style="left:604px;top:105px;width:368px;height:795px">
    <div class="brand">ZUBVI</div>
    <h1>User Login</h1>
    <div class="field">First Name</div>
    <div class="field">Last Name</div>
    <div class="submit">SUBMIT</div>
    <div class="create">Create Account</div>
    <div class="dots"><i></i><i></i><i></i><i></i><i></i></div>
  </section>

  <!-- Feed, dark -->
  <section class="screen screen--dark" style="left:1093px;top:100px">
    <header class="topbar">
      <svg viewBox="0 0 20 20" fill="none" stroke="#fff" stroke-width="2"><path d="M13 4 7 10l6 6"/></svg>
      <svg viewBox="0 0 20 20" fill="none" stroke="#fff" stroke-width="2.4"><circle cx="8.5" cy="8.5" r="5.5"/><path d="m13 13 5 5"/></svg>
    </header>
    <div class="tabs"><span class="on">ForYou</span><span>News</span></div>
    <div class="card challenge" style="top:140px">
      <h3>Daily Challenge</h3>
      <p>Lorem ipsum dolor sit amet, consectetur adipiscing elit, sed do eiusmod tempor incididunt ut labore et dolore magna aliqua.</p>
      <span class="btn-pill">Start Now ➜</span>
      <div class="rocket" role="img" aria-label="Rocket illustration launching from a circle"></div>
    </div>
    <div class="card" style="left:22px;top:345px;width:294px;height:78px;padding:10px 12px">
      <div style="font-size:15px;font-weight:500">Hey Charlie!</div>
      <div style="display:flex;align-items:center;margin-top:12px">
        <div class="avatars" role="img" aria-label="Friend avatars"><i></i><i></i><i></i></div>
        <span style="margin-left:auto;margin-right:22px;font-size:16px">8</span>
        <span class="bell" style="background:var(--violet-soft)"><svg viewBox="0 0 14 14" fill="#fff"><path d="M7 1a4 4 0 0 1 4 4v4l1 1H2l1-1V5a4 4 0 0 1 4-4zM5.5 12h3a1.5 1.5 0 0 1-3 0z"/></svg></span>
      </div>
    </div>
    <div class="card" style="left:22px;top:442px;width:294px;height:80px;padding:10px 18px;display:flex">
      <div><div style="font-size:19px">$ 543</div><div style="font-size:14px;margin-top:2px">Last Earning</div><div style="font-size:13px;margin-top:6px">$ 120</div></div>
      <div style="margin-left:38px;font-size:13px;line-height:20px;color:var(--violet-soft)"><div style="color:var(--gold);font-size:10px;letter-spacing:2px">★★★★★</div>Lumo Advertisement<br>Review</div>
    </div>
    <div class="discover" style="top:553px">Discover</div>
    <div class="brand-card" style="left:22px;top:595px"><h4>Strido.inc</h4><div class="mark"></div><small>Lorem ipsum dolor<br>sit amet</small><span class="follow">Follow</span></div>
    <div class="brand-card" style="left:154px;top:595px"><h4>Vantor.inc</h4><div class="mark"></div><small>Lorem ipsum dolor<br>sit amet</small><span class="follow">Follow</span></div>
    <div class="brand-card" style="left:284px;top:595px"><h4>Kelso.inc</h4><div class="mark"></div><small>Lorem ipsum dolor<br>sit amet</small><span class="follow">Follow</span></div>
    <div class="brand-card" style="left:22px;top:745px"><h4>Ardent.inc</h4><div class="mark"></div></div>
    <div class="brand-card" style="left:154px;top:745px"><h4>Pacewell</h4><div class="mark"></div></div>
    <div class="brand-card" style="left:284px;top:745px"><h4>Strido.inc</h4><div class="mark"></div></div>
  </section>

  <!-- About, light -->
  <section class="screen screen--light" style="left:105px;top:1048px">
    <header class="topbar">
      <svg viewBox="0 0 20 20" fill="none" stroke="#111" stroke-width="2"><path d="M13 4 7 10l6 6"/></svg>
      <span class="wordmark">ZUBVI</span>
      <svg viewBox="0 0 20 20" fill="none" stroke="#111" stroke-width="2.4"><circle cx="8.5" cy="8.5" r="5.5"/><path d="m13 13 5 5"/></svg>
    </header>
    <div class="photo" role="img" aria-label="Photo of young friends sitting in a row looking at their phones"></div>
    <article class="about">
      <h2>About Zubvi</h2><div class="rule"></div>
      <p>Lorem ipsum dolor sit amet, consectetur adipiscing elit, sed do eiusmod tempor incididunt ut labore et dolore magna aliqua. Quis ipsum suspendisse ultrices gravida. Risus commodo viverra maecenas accumsan lacus vel facilisis. Lorem ipsum dolor sit amet, consectetur adipiscing elit, sed do eiusmod tempor incididunt ut labore et dolore magna aliqua. Quis ipsum suspendisse ultrices gravida. Risus commodo viverra maecenas accumsan lacus vel facilisis.</p>
    </article>
    <nav class="tabbar">
      <div class="tab"><svg viewBox="0 0 26 26" fill="none" stroke-width="1.8"><path d="M4 8h18M4 13h18M4 18h18"/></svg>Home</div>
      <div class="tab"><svg viewBox="0 0 26 26" fill="none" stroke-width="1.5"><path d="M3 5h20l-1 5H4zM5 10v12h16V10M10 22v-6h6v6"/></svg>Marketplace</div>
      <div class="tab"><svg viewBox="0 0 26 26" fill="none" stroke-width="1.5"><rect x="4" y="8" width="18" height="14" rx="2"/><path d="M7 8l9-4 2 4M16 13h6v5h-6z"/></svg>Vault</div>
      <div class="tab"><svg viewBox="0 0 26 26" fill="none" stroke-width="1.5"><circle cx="13" cy="13" r="11"/><circle cx="13" cy="10" r="4"/><path d="M6 20c2-4 12-4 14 0"/></svg>Profile</div>
    </nav>
  </section>

  <!-- Login, light -->
  <section class="screen login login--light" style="left:599px;top:1050px">
    <div class="brand">ZUBVI</div>
    <h1>User Login</h1>
    <div class="field">First Name</div>
    <div class="field">Last Name</div>
    <div class="submit">SUBMIT</div>
    <div class="create">Create Account</div>
    <div class="dots"><i></i><i></i><i></i><i></i><i></i></div>
  </section>

  <!-- Feed, light -->
  <section class="screen screen--light" style="left:1093px;top:1047px;background:var(--white)">
    <header class="topbar">
      <svg viewBox="0 0 20 20" fill="none" stroke="#111" stroke-width="2"><path d="M13 4 7 10l6 6"/></svg>
      <svg viewBox="0 0 20 20" fill="none" stroke="#111" stroke-width="2.4"><circle cx="8.5" cy="8.5" r="5.5"/><path d="m13 13 5 5"/></svg>
    </header>
    <div class="tabs"><span class="on">ForYou</span><span>News</span></div>
    <div class="card challenge" style="top:140px">
      <h3>Daily Challenge</h3>
      <p>Lorem ipsum dolor sit amet, consectetur adipiscing elit, sed do eiusmod tempor incididunt ut labore et dolore magna aliqua.</p>
      <span class="btn-pill">Start Now ➜</span>
      <div class="rocket" role="img" aria-label="Rocket illustration launching from a circle"></div>
    </div>
    <div class="card" style="left:22px;top:362px;width:150px;height:125px;padding:10px 12px;background:linear-gradient(135deg,var(--hot-pink),var(--violet));color:#fff;box-shadow:none">
      <div style="font-size:15px;font-weight:500">Hey Charlie!</div>
      <div class="avatars" style="margin-top:14px" role="img" aria-label="Friend avatars"><i></i><i></i><i></i></div>
      <div style="display:flex;align-items:center;margin-top:12px"><span style="font-size:16px">8</span>
        <span class="bell" style="background:#fff;margin-left:auto"><svg viewBox="0 0 14 14" fill="#ff3d8a"><path d="M7 1a4 4 0 0 1 4 4v4l1 1H2l1-1V5a4 4 0 0 1 4-4zM5.5 12h3a1.5 1.5 0 0 1-3 0z"/></svg></span></div>
    </div>
    <div class="card" style="left:198px;top:362px;width:150px;height:125px;padding:8px 11px">
      <div style="font-size:19px;color:var(--hot-pink)">$ 543</div><div style="font-size:14px">Last Earning</div><div style="font-size:13px;margin-top:6px">$ 120</div>
      <div style="font-size:13px;line-height:20px;color:var(--violet-soft);margin-top:4px">Lumo Advertisement Review</div>
    </div>
    <div class="discover" style="top:493px;color:var(--ink)">Discover</div>
    <div class="brand-card" style="left:22px;top:533px"><div class="mark"></div><h4>Strido.inc</h4><small>Lorem ipsum dolor sit<br>amet, consectetur</small><span class="follow">Follow</span></div>
    <div class="brand-card" style="left:231px;top:533px"><div class="mark"></div><h4>Lynxa.inc</h4><small>Lorem ipsum dolor sit<br>amet, consectetur</small><span class="follow">Follow</span></div>
    <div class="brand-card" style="left:22px;top:648px"><div class="mark"></div><h4>Ardent.inc</h4><small>Lorem ipsum dolor sit<br>amet, consectetur</small><span class="follow">Follow</span></div>
    <div class="brand-card" style="left:231px;top:648px"><div class="mark"></div><h4>Vantor.inc</h4><small>Lorem ipsum dolor sit<br>amet, consectetur</small><span class="follow">Follow</span></div>
    <nav class="tabbar">
      <div class="tab"><svg viewBox="0 0 26 26" fill="none" stroke-width="1.8"><path d="M4 8h18M4 13h18M4 18h18"/></svg>Home</div>
      <div class="tab"><svg viewBox="0 0 26 26" fill="none" stroke-width="1.5"><path d="M3 5h20l-1 5H4zM5 10v12h16V10M10 22v-6h6v6"/></svg>Marketplace</div>
      <div class="tab"><svg viewBox="0 0 26 26" fill="none" stroke-width="1.5"><rect x="4" y="8" width="18" height="14" rx="2"/><path d="M7 8l9-4 2 4M16 13h6v5h-6z"/></svg>Vault</div>
      <div class="tab"><svg viewBox="0 0 26 26" fill="none" stroke-width="1.5"><circle cx="13" cy="13" r="11"/><circle cx="13" cy="10" r="4"/><path d="M6 20c2-4 12-4 14 0"/></svg>Profile</div>
    </nav>
  </section>
</div>
</body>
</html>
```